Flower delivery business needs sales brochure

I have a courier business that specialises in same-day flower deliveries; I want to make a single page A4 sales brochure (folded to DL) to give to our potential customers.
The company website is petalcouriers.net, this will give an idea of who we are and what we do, as well as some graphics and colours that we use.
When opened, the inside A4 space of the brochure will be a pricelist, so the entire page will be an excel table with delivery locations and prices; we will add the prices ourselves later, so ideally the inside will be a background of some sort that won't obstruct text. Maybe light/transparent flowers and a background colour?
The front of the DL brochure should be mostly a title page, so business name, phone number, a graphic?
The first inside page should relate to our service, there's a lot of info on our website that you could use, so same day delivery, 10:30 and 2:30 pick-up times, established over 10 years ago, air-conditioned vans, delivery to 300+ suburbs.
The back page would be contact details and maybe a summary of the key points of the 'about us' section of the website.

Industry/Entity Type

Business

```html
<!DOCTYPE html>
<html lang="en">
<head>
<meta charset="utf-8">
<title>Petal Couriers – DL Brochure</title>
<link rel="stylesheet" href="https://fonts.googleapis.com/css2?family=Aldrich&family=Roboto+Condensed:ital,wght@0,400;0,700;1,400&display=swap">
<style>
  :root {
    --orange: #f2673a;
    --amber: #f9a431;
    --yellow: #fdc82e;
    --green: #6aa251;
    --grass-dark: #4d7a2a;
    --grass-light: #9cc25a;
    --white: #ffffff;
    --ink-soft: #f2f7ee;
    --page: #ffffff;
  }
  * { box-sizing: border-box; margin: 0; padding: 0; }
  html, body { width: 1200px; height: 663px; overflow: hidden; background: var(--page); }
  body { position: relative; font-family: "Roboto Condensed", Arial, sans-serif; color: var(--white); }

  .spread {
    position: absolute; top: 136px; width: 555px; height: 390px; overflow: hidden;
    background: linear-gradient(180deg, var(--orange) 0%, var(--amber) 22%, var(--yellow) 45%, var(--yellow) 100%);
  }
  .spread--outside { left: 30px; }
  .spread--inside { left: 615px; }

  .grass-band {
    position: absolute; left: 0; right: 0; bottom: 0; height: 118px;
    background: linear-gradient(180deg, rgba(156,194,90,0) 0%, var(--grass-light) 35%, var(--grass-dark) 100%);
  }

  .panel { position: absolute; background: var(--green); text-align: center; }
  .panel__title {
    font-family: "Aldrich", "Arial Narrow", sans-serif; font-weight: 400;
    font-size: 14px; line-height: 1.45; letter-spacing: 0.3px; text-transform: uppercase;
  }
  .panel__dot {
    display: inline-block; width: 11px; height: 11px; border-radius: 50%;
    background: #ee7fa0; margin-right: 6px; vertical-align: -1px;
  }

  /* Back page */
  .panel--back { left: 18px; top: 14px; width: 272px; height: 252px; padding: 20px 18px 0; }
  .panel--back .attribution { font-size: 4px; text-align: right; margin: 1px 28px 12px 0; opacity: 0.9; }
  .panel--back p { font-size: 6px; line-height: 1.35; margin-bottom: 8px; }
  .panel--back .contact { font-weight: 700; font-size: 6.2px; }

  /* Front page */
  .flower-cluster {
    position: absolute; left: 300px; top: 60px; width: 240px; height: 250px; border-radius: 50%;
    background: radial-gradient(circle at 50% 45%, rgba(233,69,47,0.55) 0%, rgba(240,150,40,0.35) 45%, rgba(253,200,46,0) 72%);
  }
  .brand {
    position: absolute; left: 300px; top: 168px; width: 240px; text-align: center;
    font-family: "Aldrich", "Arial Narrow", sans-serif; font-size: 27px; color: var(--green);
  }
  .brand__mark {
    display: inline-block; width: 12px; height: 12px; border-radius: 50%;
    background: var(--green); margin-right: 6px; vertical-align: 3px;
  }
  .web-bar {
    position: absolute; left: 318px; bottom: 18px; width: 225px; height: 22px;
    background: var(--green); clip-path: polygon(0 18%, 100% 0, 100% 82%, 0 100%);
    display: flex; align-items: center; justify-content: space-between; padding: 0 9px;
    font-weight: 700; font-size: 9.5px; letter-spacing: 0.4px;
  }

  /* Inside */
  .price-page {
    position: absolute; left: 18px; top: 15px; width: 255px; height: 375px;
    background: linear-gradient(180deg, var(--white) 0%, #fff6d8 40%, rgba(253,200,46,0.6) 100%);
  }
  .panel--service {
    right: 17px; top: 18px; width: 243px; height: 260px; padding: 20px 14px 0;
    clip-path: polygon(0 0, 100% 0, 100% 100%, 0 90%);
  }
  .panel--service .panel__title { font-size: 13.5px; text-transform: uppercase; margin-bottom: 14px; }
  .panel--service p { font-size: 8.3px; line-height: 1.5; }
  .quote { position: relative; margin-top: 14px; font-style: italic; padding: 0 6px; }
  .quote__mark {
    position: absolute; font-family: Georgia, serif; font-style: normal; font-weight: 700;
    font-size: 18px; color: var(--yellow); line-height: 1;
  }
  .quote__mark--open { left: -6px; top: -3px; }
  .quote__mark--close { right: -6px; bottom: -14px; }
</style>
</head>
<body>

  <section class="spread spread--outside" aria-label="Outside spread: back and front pages">
    <div class="panel panel--back">
      <h2 class="panel__title"><span class="panel__dot"></span>"Superior in service<br>and efficiency"</h2>
      <div class="attribution">Bloomfield Florist</div>
      <p>Our service offers pick-ups twice a day for those florists<br>whose volume requires it:<br>a mid-morning pick-up prior to our depot - handover at 10:30am<br>an afternoon pick-up prior to our second depot - handover at 2:30pm</p>
      <p>Most flowers are delivered within 4/5 hours after pick-up.<br>Local (ie within area of pickup location)<br>and timed deliveries are given priority and we can<br>accommodate for special deadlines with prior notice.</p>
      <p class="contact">Contact Us: Operations: 0400 555 123<br>(9am-5pm Mon-Fri &amp; 9am-3pm Sat)</p>
      <p class="contact">NEW CUSTOMER OR HAVE AN ADMINISTRATION /<br>BILLING QUERY? Email Us: info@petalcouriers.net</p>
      <p class="contact">Postal Address:<br>PO Box 4410, Kelvin Grove DC, QLD, 4059</p>
    </div>

    <div class="flower-cluster" role="img" aria-label="Circle of sunflowers, poppies, pansies, gerberas, a tulip and a daffodil around the brand name"></div>
    <div class="brand"><span class="brand__mark"></span>Petal Couriers</div>

    <div class="grass-band" role="img" aria-label="Green grass with pansies, poppies, sunflowers, gerberas and daffodils"></div>

    <div class="web-bar"><span>www.petalcouriers.net</span><span>PH: 0400 555 123</span></div>
  </section>

  <section class="spread spread--inside" aria-label="Inside spread">
    <div class="price-page"></div>
    <div class="grass-band" role="img" aria-label="Green grass with a row of pansies, sunflowers, gerberas, poppies and daffodils"></div>

    <div class="panel panel--service">
      <h2 class="panel__title"><span class="panel__dot"></span>Flowers straight<br>to your front door</h2>
      <p>Petal Couriers Pty Ltd is a courier company that specializes in the delivery of flowers and gifts. We offer a same day courier service for the florist &amp; gift retail and wholesale market, and deliver to over 300 suburbs throughout the Brisbane Metropolitan region.</p>
      <p class="quote">
        <span class="quote__mark quote__mark--open">&ldquo;</span>
        We have been in the business for over 10 years, and are very focused on delivering the best customer service possible.
        <span class="quote__mark quote__mark--close">&rdquo;</span>
      </p>
    </div>
  </section>

</body>
</html>
```